Rework of existing brochure designs

Replace Logo(s) with images provided
Company and website
Minor changes in text

-------------
Second file (Brevant Assurance) to be redesigned into same design as Quillex Brochure

Did not get the level of creative reequired

```html
<!DOCTYPE html>
<html lang="en">
<head>
<meta charset="utf-8">
<title>Quillex Services Brochure – NimbusWorks</title>
<link rel="stylesheet" href="https://fonts.googleapis.com/css2?family=Open+Sans:wght@400;600;700&display=swap">
<style>
:root{
  --brand-blue:#2a6fb3;
  --text-dark:#333b45;
  --text-body:#555c66;
  --rule:#d9dde2;
  --footer-bg:#e9ebee;
  --badge-blue:#1f8fd0;
  --page-bg:#ffffff;
}
*{box-sizing:border-box;margin:0;padding:0}
html,body{width:853px;height:1200px;overflow:hidden;background:var(--page-bg)}
body{font-family:"Open Sans",Arial,sans-serif;color:var(--text-body);position:relative}
.offer{position:absolute;left:0;width:853px}
.offer--quick-win{top:115px}
.offer--assurance{top:645px}
.offer__aside{position:absolute;left:85px;width:290px}
.offer__title{font-size:15px;font-weight:700;letter-spacing:.5px;color:var(--brand-blue);text-transform:uppercase;line-height:1.35}
.aside-list{margin-top:12px;list-style:none;font-size:12.5px;line-height:1.55}
.aside-list li{position:relative;padding-left:14px;margin-bottom:2px}
.aside-list li::before{content:"";position:absolute;left:0;top:9px;width:5px;height:1px;background:var(--text-body)}
.offer__main{position:absolute;left:455px;width:340px}
.offer__lead{font-size:13.5px;font-weight:700;color:var(--text-dark);line-height:1.5}
.offer__scope{margin-top:16px;font-size:13px;line-height:1.5}
.main-list{margin-top:14px;list-style:none;font-size:13.5px;line-height:1.5}
.main-list li{position:relative;padding-left:20px;margin-bottom:10px}
.main-list li::before{content:"";position:absolute;left:2px;top:9px;width:5px;height:5px;border-radius:50%;background:var(--text-body)}
.column-rule{position:absolute;left:420px;top:110px;width:1px;height:860px;background:var(--rule)}
.about{position:absolute;left:85px;top:1000px;width:600px}
.about__title{font-size:12px;font-weight:700;color:var(--text-dark)}
.about__text{margin-top:4px;font-size:11.5px;line-height:1.45;text-align:justify}
.partner-badge{position:absolute;left:705px;top:1025px}
.footer{position:absolute;left:0;top:1155px;width:853px;height:45px;background:var(--footer-bg);display:flex;justify-content:space-between;align-items:center;padding:0 85px;font-size:13px;color:var(--text-dark)}
</style>
</head>
<body>
<div class="column-rule"></div>

<section class="offer offer--quick-win">
  <div class="offer__aside">
    <h2 class="offer__title">One Day Quick Win</h2>
    <ul class="aside-list">
      <li>Solutions improvement</li>
      <li>Knowledge Share</li>
      <li>Investigate Complimentary Solutions</li>
      <li>Configuration Health Check</li>
      <li>Post Implementation Refinements</li>
      <li>Process improvement</li>
    </ul>
  </div>
  <div class="offer__main">
    <p class="offer__lead">Get up and running in a day with this fast track configuration. Everything you need to be maximising your ROI from day one!</p>
    <p class="offer__scope">Scope: Everything we can get done one day. Choose from some of these.</p>
    <ul class="main-list">
      <li>Campaign Design and Flow</li>
      <li>Lead Smart List management and status updates</li>
      <li>Build Landing Pages and Forms</li>
      <li>Track Web Page Visitor behaviour</li>
      <li>Drip feed email marketing and responses</li>
      <li>Measure Campaign Results</li>
      <li>Integrate with Cirrusdesk.com</li>
      <li>Build Knowledge</li>
    </ul>
  </div>
</section>

<section class="offer offer--assurance">
  <div class="offer__aside">
    <h2 class="offer__title">Brevant<br>Assurance</h2>
    <ul class="aside-list">
      <li>Build an extended support package that is tailored to your level of expertise and goals</li>
      <li>Maintain and grow adoption and secure the future of your Quillex solution and maximise your ROI</li>
    </ul>
  </div>
  <div class="offer__main">
    <p class="offer__lead">A flexible monthly solution based support plan tailored to your unique requirements.</p>
    <p class="offer__scope">Scope: Total flexibility for tailor made solutions support.</p>
    <ul class="main-list">
      <li>Service Level Agreements</li>
      <li>Dedicated Solutions Administrator</li>
      <li>Regular Solution Health Check</li>
      <li>Knowledge Share</li>
      <li>Solutions Enhancements</li>
      <li>Telephone Assistance</li>
    </ul>
  </div>
</section>

<section class="about">
  <h3 class="about__title">About NimbusWorks</h3>
  <p class="about__text">Created in 2009, NimbusWorks are one of the longest established Cirrusdesk.com core partners in the UK with a history of over 25 years in business management consulting, business process improvement and now Cloud Transformation and innovation. We provide dynamic and trust worthy advice, knowledge and expertise with a range of different consulting styles to complement your organisation's personality and aspirations.</p>
</section>

<svg class="partner-badge" width="90" height="55" viewBox="0 0 90 55" role="img" aria-label="Registered consulting partner badge">
  <rect x="0" y="0" width="90" height="55" rx="8" fill="var(--badge-blue)"/>
</svg>

<footer class="footer">
  <span class="footer__phone">0800 555 0192</span>
  <span class="footer__web">nimbusworks.co.uk</span>
</footer>
</body>
</html>
```